A online shop for solid wood need a Stationary design

A new online shop (in Austria and Germany) for solid wood and steel furniture (feldmark-tischwerk) needs a Stationay design (letterhead, business card, envelope etc...). Dining tables, coffee tables, TV furniture and similar furniture will be sold. Everything will be custom made.

```html
<!DOCTYPE html>
<html lang="de">
<head>
<meta charset="utf-8">
<title>Feldmark Tischwerk – Geschäftsausstattung</title>
<link href="https://fonts.googleapis.com/css2?family=Questrial&family=Lato:wght@400;700&family=Tinos&display=swap" rel="stylesheet">
<style>
  :root {
    --bg: #2b2b2b;
    --paper: #ffffff;
    --paper-shade: #ececec;
    --ink: #1d1213;
    --rule: #b9b9b9;
    --text: #222;
    --light: #f4f4f4;
    --sign: #1f2a8a;
  }
  * { margin: 0; padding: 0; box-sizing: border-box; }
  html, body { width: 1200px; height: 900px; overflow: hidden; }
  body { background: var(--bg); position: relative; font-family: "Lato", sans-serif; color: var(--text); }

  .set-title {
    position: absolute; right: 46px; top: 34px;
    font-family: "Questrial", sans-serif; font-size: 46px; color: var(--paper); letter-spacing: -0.5px;
  }

  /* Wordmark */
  .wordmark { position: absolute; display: flex; flex-direction: column; align-items: center; color: var(--ink); font-family: "Lato", sans-serif; font-weight: 700; text-align: center; }
  .wordmark .mark-square { background: var(--ink); }
  .wordmark .name { line-height: 1; letter-spacing: 1px; }
  .wordmark .sub { line-height: 1; letter-spacing: 1.5px; }
  .wordmark.invert { color: var(--paper); }
  .wordmark.invert .mark-square { background: var(--paper); }

  /* Letterhead */
  .letterhead {
    position: absolute; left: 172px; top: 235px; width: 425px; height: 550px;
    background: linear-gradient(180deg, var(--paper-shade) 0, var(--paper) 40px);
  }
  .letterhead .frame-top { position: absolute; left: 38px; top: 87px; width: 334px; height: 1px; background: var(--rule); }
  .letterhead .frame-left { position: absolute; left: 38px; top: 87px; width: 1px; height: 420px; background: var(--rule); }
  .letterhead .wordmark { right: 53px; top: 18px; }
  .letter-body { position: absolute; left: 57px; top: 126px; width: 316px; font-family: "Tinos", serif; font-size: 7.9px; line-height: 9.2px; color: #111; }
  .recipient { display: flex; gap: 14px; margin-bottom: 20px; }
  .letter-body p { margin-bottom: 9px; }
  .signature { width: 96px; height: 26px; margin-top: 2px; background: linear-gradient(90deg, #dfe2f2, #eef0fa); }
  .letter-footer { position: absolute; left: 0; bottom: 0; width: 100%; height: 37px; display: flex; font-size: 5.2px; }
  .letter-footer div { display: flex; align-items: center; }
  .letter-footer .addr { width: 183px; padding-left: 57px; }
  .letter-footer .phone { width: 114px; justify-content: center; border-left: 1px solid var(--rule); }
  .letter-footer .fax { flex: 1; justify-content: flex-end; padding-right: 52px; border-left: 1px solid var(--rule); }

  /* Envelope */
  .envelope { position: absolute; left: 545px; top: 430px; width: 475px; height: 274px; }
  .envelope .flap {
    position: absolute; left: 4px; top: 0; width: 467px; height: 68px;
    background: var(--ink); border-radius: 12px 12px 0 0;
  }
  .flap-inner { position: absolute; inset: 0; transform: rotate(180deg); color: var(--paper); }
  .flap-inner .tagline { position: absolute; left: 198px; top: 18px; }
  .flap-inner .wordmark { left: 360px; top: 10px; }
  .flap-inner .web { position: absolute; left: 378px; bottom: 5px; font-size: 4.6px; }
  .envelope .body {
    position: absolute; left: 0; top: 68px; width: 475px; height: 206px;
    background: linear-gradient(180deg, var(--paper-shade) 0, var(--paper) 40px);
  }
  .envelope .body .wordmark { left: 28px; top: 59px; }
  .env-contact { position: absolute; left: 16px; top: 133px; font-size: 5.2px; }
  .env-contact .row { width: 120px; text-align: center; padding: 7px 0; }
  .env-contact .row:first-child { text-align: left; padding-top: 0; }
  .env-contact .divider { width: 36px; height: 1px; background: var(--rule); margin-left: 42px; }

  .tagline { text-align: center; font-family: "Lato", sans-serif; font-size: 10px; letter-spacing: 1.2px; line-height: 1.15; }
  .tagline .mid { font-size: 5px; letter-spacing: 7px; }

  /* Business cards */
  .card { position: absolute; border-radius: 9px; }
  .card-front { left: 825px; top: 242px; width: 96px; height: 170px; background: var(--ink); color: var(--paper); }
  .card-front .wordmark { left: 0; right: 0; top: 18px; }
  .card-front .tagline { position: absolute; left: 0; right: 0; top: 70px; }
  .card-front .web { position: absolute; left: 0; right: 0; bottom: 8px; text-align: center; font-size: 4.6px; }
  .card-back { left: 907px; top: 366px; width: 96px; height: 172px; background: var(--light); color: var(--text); }
  .card-back .wordmark { left: 0; right: 0; top: 18px; }
  .card-back .person { position: absolute; left: 0; right: 0; top: 70px; text-align: center; }
  .person .name { font-weight: 700; font-size: 6px; }
  .person .role { font-size: 3.8px; }
  .card-back .details { position: absolute; left: 0; right: 0; top: 90px; text-align: center; font-size: 3.8px; }
  .details .line { padding: 5px 0; }
  .details .divider { width: 36px; height: 1px; background: var(--rule); margin: 0 auto; }
</style>
</head>
<body>

<div class="set-title">Feldmark Tischwerk</div>

<!-- Letterhead -->
<section class="letterhead">
  <div class="wordmark">
    <span class="mark-square" style="width:20px;height:20px;margin-bottom:5px"></span>
    <span class="name" style="font-size:12px">FELDMARK</span>
    <span class="sub" style="font-size:5px;margin-top:2px">TISCHWERK</span>
  </div>
  <div class="frame-top"></div>
  <div class="frame-left"></div>

  <div class="letter-body">
    <div class="recipient">
      <span>To:</span>
      <span>Mr./Mrs. Customerand Partner<br>42 Maple Street<br>New York<br>NY 55254</span>
    </div>
    <p>Dear Customer,</p>
    <p>Lorem ipsum dolor sit amet, consetetur sadipscing elitr, sed diam nonumy eirmod tempor invidunt ut labore et dolore magna aliquyam erat, sed diam voluptua. At vero eos et accusam et justo duo dolores et ea rebum. Stet clita kasd gubergren, no sea takimata sanctus est Lorem ipsum dolor sit amet. Lorem ipsum dolor sit amet, consetetur sadipscing elitr, sed diam nonumy eirmod tempor invidunt ut labore et dolore magna aliquyam erat, sed diam voluptua. At vero eos et accusam et justo duo dolores et ea rebum. Stet clita kasd gubergren, no sea takimata sanctus est Lorem ipsum dolor sit amet. Lorem ipsum dolor sit amet, consetetur sadipscing elitr, sed diam nonumy eirmod tempor invidunt ut labore et dolore magna aliquyam erat, sed diam voluptua. At vero eos et accusam et justo duo dolores et ea rebum. Stet clita kasd gubergren, no sea takimata sanctus est Lorem ipsum dolor sit amet.</p>
    <p>Duis autem vel eum iriure dolor in hendrerit in vulputate velit esse molestie consequat, vel illum dolore eu feugiat nulla facilisis at vero eros et accumsan et iusto odio dignissim qui blandit praesent luptatum zzril delenit augue duis dolore te feugait nulla facilisi. Lorem ipsum dolor sit amet, consectetuer adipiscing elit, sed diam nonummy nibh euismod tincidunt ut laoreet dolore magna aliquam erat volutpat.</p>
    <p>Nam liber tempor cum soluta nobis eleifend option congue nihil imperdiet doming id quod mazim placerat facer possim assum. Lorem ipsum dolor sit amet, consectetuer adipiscing elit, sed diam nonummy nibh euismod tincidunt ut laoreet dolore magna aliquam erat volutpat. Ut wisi enim ad minim veniam, quis nostrud exerci tation ullamcorper suscipit lobortis nisl ut aliquip ex ea commodo consequat.</p>
    <div>Sincerely,</div>
    <div class="signature" role="img" aria-label="Handwritten signature of Lukas Berger"></div>
  </div>

  <footer class="letter-footer">
    <div class="addr">1820 Birchwood Lane Denver, CO 80202</div>
    <div class="phone"><b>P:</b>&nbsp;303-555-0140</div>
    <div class="fax"><b>F:</b>&nbsp;303-555-0141</div>
  </footer>
</section>

<!-- Envelope -->
<section class="envelope">
  <div class="body">
    <div class="wordmark">
      <span class="mark-square" style="width:18px;height:18px;margin-bottom:5px"></span>
      <span class="name" style="font-size:11px">FELDMARK</span>
      <span class="sub" style="font-size:4.6px;margin-top:2px">TISCHWERK</span>
    </div>
    <div class="env-contact">
      <div class="row">1820 Birchwood Lane Denver, CO 80202</div>
      <div class="divider"></div>
      <div class="row"><b>P:</b> 303-555-0140</div>
      <div class="divider"></div>
      <div class="row"><b>F:</b> 303-555-0141</div>
    </div>
  </div>
  <div class="flap">
    <div class="flap-inner">
      <div class="tagline">EVERYTHING<br><span class="mid">WILL BE</span><br>CUSTOM MADE</div>
      <div class="wordmark invert">
        <span class="mark-square" style="width:14px;height:14px;margin-bottom:4px"></span>
        <span class="name" style="font-size:8.5px">FELDMARK</span>
        <span class="sub" style="font-size:3.6px;margin-top:1px">TISCHWERK</span>
      </div>
      <div class="web">www.feldmark-tischwerk.at</div>
    </div>
  </div>
</section>

<!-- Business card front -->
<section class="card card-front">
  <div class="wordmark invert">
    <span class="mark-square" style="width:14px;height:14px;margin-bottom:4px"></span>
    <span class="name" style="font-size:8.5px">FELDMARK</span>
    <span class="sub" style="font-size:3.6px;margin-top:1px">TISCHWERK</span>
  </div>
  <div class="tagline">EVERYTHING<br><span class="mid">WILL BE</span><br>CUSTOM MADE</div>
  <div class="web">www.feldmark-tischwerk.at</div>
</section>

<!-- Business card back -->
<section class="card card-back">
  <div class="wordmark">
    <span class="mark-square" style="width:14px;height:14px;margin-bottom:4px"></span>
    <span class="name" style="font-size:8.5px">FELDMARK</span>
    <span class="sub" style="font-size:3.6px;margin-top:1px">TISCHWERK</span>
  </div>
  <div class="person">
    <div class="name">Lukas Berger</div>
    <div class="role">President</div>
  </div>
  <div class="details">
    <div class="line">lukasberger@feldmark-tischwerk.at</div>
    <div class="divider"></div>
    <div class="line"><b>M:</b> 01-555-0142</div>
    <div class="divider"></div>
    <div class="line"><b>P:</b> 303-555-0140</div>
    <div class="divider"></div>
    <div class="line"><b>F:</b> 303-555-0141</div>
    <div class="divider"></div>
    <div class="line">1820 Birchwood Lane Denver, CO 80202</div>
  </div>
</section>

</body>
</html>
```